Professional and creative business card design for recruiting service providers

Our company supports German medium-sized companies in filling vacancies promptly. For this we use social media marketing and bring our customers into the visibility.

We want a professional but also creative design for our business cards.

Please look at halvenrick-consult.de to get an impression of our CI.

Target Market(s)

Small and medium-sized companies in Germany from the industry

Industry/Entity Type

Industrie, Handwerk

Contact Information for Business Card

Name, Position, Telefonnummer, Email, Website

Colors
EE7325
F08F49
F5BC92
FAE3D3
FDF4ED

Requirements
Must have
• A picture of the employee and in the style of www.halvenrick-consult.de

```html
<!DOCTYPE html>
<html lang="de">
<head>
<meta charset="utf-8">
<title>Halvenrick Consult – Visitenkarte</title>
<link rel="stylesheet" href="https://fonts.googleapis.com/css2?family=Montserrat:wght@400;500;700;800&display=swap">
<style>
  :root {
    --orange: #ee5f2a;
    --orange-soft: #f08f49;
    --paper: #f7f7f7;
    --ink: #222222;
    --stage: #333333;
    --card-dark: #1b1b1b;
    --card-dark-2: #262626;
    --white: #ffffff;
  }
  * { box-sizing: border-box; margin: 0; padding: 0; }
  html, body { width: 1200px; height: 1200px; overflow: hidden; }
  body {
    background: var(--stage);
    font-family: "Montserrat", Arial, sans-serif;
    position: relative;
  }
  .card {
    position: absolute;
    left: 190px;
    width: 820px;
    height: 500px;
    border-radius: 34px;
    overflow: hidden;
    box-shadow: 0 18px 40px rgba(0,0,0,.45);
  }
  /* Front */
  .card--front { top: 70px; background: var(--paper); }
  .front-accent { position: absolute; inset: 0; width: 100%; height: 100%; }
  .portrait {
    position: absolute;
    left: 520px; top: 110px;
    width: 300px; height: 390px;
    border-radius: 120px 120px 0 0;
    background: linear-gradient(180deg, #6b4a3a 0%, #2a2a34 35%, #15151c 100%);
  }
  .notch {
    position: absolute; left: 0; top: 292px;
    width: 0; height: 0;
    border-top: 20px solid transparent;
    border-bottom: 20px solid transparent;
    border-left: 24px solid var(--orange);
  }
  .identity { position: absolute; left: 56px; top: 250px; }
  .identity__name {
    color: var(--orange); font-weight: 800; font-size: 36px; letter-spacing: .5px; line-height: 1;
  }
  .identity__role { color: var(--ink); font-weight: 500; font-size: 26px; margin-top: 4px; }
  .contacts { list-style: none; margin-top: 22px; }
  .contacts__item {
    display: flex; align-items: flex-start; gap: 16px;
    color: var(--ink); font-size: 19px; line-height: 1.15; margin-bottom: 12px;
  }
  .contacts__icon { width: 22px; height: 22px; flex: none; margin-top: 1px; }
  /* Back */
  .card--back {
    top: 630px;
    background: linear-gradient(120deg, var(--card-dark) 0%, var(--card-dark-2) 55%, var(--card-dark) 100%);
  }
  .brand {
    position: absolute; left: 170px; top: 180px;
    display: flex; align-items: center; gap: 28px;
  }
  .brand__square { width: 90px; height: 90px; background: var(--orange); }
  .brand__name {
    color: var(--white); font-weight: 800; font-size: 46px; letter-spacing: 5px; line-height: 1.1;
  }
  .web {
    position: absolute; right: 60px; top: 380px;
    color: var(--white); font-size: 24px; letter-spacing: .5px;
  }
  .web-bar {
    position: absolute; left: 400px; right: 60px; top: 425px; height: 16px;
    background: var(--orange);
  }
</style>
</head>
<body>
  <section class="card card--front">
    <svg class="front-accent" viewBox="0 0 820 500" aria-hidden="true">
      <polygon points="490,0 820,0 820,500 560,500" fill="var(--orange)"/>
    </svg>
    <div class="portrait" role="img" aria-label="Porträtfoto des Gründers im dunklen Sakko"></div>
    <span class="notch"></span>
    <div class="identity">
      <h1 class="identity__name">Jonas Halvenrick</h1>
      <p class="identity__role">Gründer</p>
      <ul class="contacts">
        <li class="contacts__item">
          <svg class="contacts__icon" viewBox="0 0 24 24"><path fill="var(--orange)" d="M6.6 10.8a15 15 0 0 0 6.6 6.6l2.2-2.2c.3-.3.7-.4 1-.2 1.1.4 2.3.6 3.6.6.6 0 1 .4 1 1V20c0 .6-.4 1-1 1A17 17 0 0 1 3 4c0-.6.4-1 1-1h3.5c.6 0 1 .4 1 1 0 1.3.2 2.5.6 3.6.1.3 0 .7-.2 1z"/></svg>
          <span>0172 394 2715</span>
        </li>
        <li class="contacts__item">
          <svg class="contacts__icon" viewBox="0 0 24 24"><path fill="var(--orange)" d="M2 5h20v14H2z"/><path d="M2 5l10 8 10-8" fill="none" stroke="#fff" stroke-width="2"/></svg>
          <span>info@halvenrick-consult.de</span>
        </li>
        <li class="contacts__item">
          <svg class="contacts__icon" viewBox="0 0 24 24"><path fill="var(--orange)" d="M12 2a7 7 0 0 0-7 7c0 5 7 13 7 13s7-8 7-13a7 7 0 0 0-7-7zm0 9.5A2.5 2.5 0 1 1 12 6.5a2.5 2.5 0 0 1 0 5z"/></svg>
          <span>Halvenrick Consult GmbH<br>Kastanienallee 27<br>70180 Stuttgart</span>
        </li>
      </ul>
    </div>
  </section>

  <section class="card card--back">
    <div class="brand">
      <span class="brand__square"></span>
      <p class="brand__name">HALVENRICK<br>CONSULT</p>
    </div>
    <p class="web">www.halvenrick-consult.de</p>
    <span class="web-bar"></span>
  </section>
</body>
</html>
```